Letterhead Design Project

Attached is our new Logo and a copy of our old letter head
Looking to rebrand with our new logo

Reason: I want to show a business card design

Industry/Entity Type

Film Production

Colors

Designer to choose colors to be used in the design.

Requirements
Must have
• The information on the old letterhead

```html
<!DOCTYPE html>
<html lang="en">
<head>
<meta charset="utf-8">
<title>Kora International – Letterhead &amp; Business Card</title>
<link rel="stylesheet" href="https://fonts.googleapis.com/css2?family=Source+Sans+3:wght@400;600;700&display=swap">
<style>
  :root {
    --blue: #1a8fcf;
    --orange: #f7941d;
    --red-orange: #ef5a24;
    --yellow: #f6e61a;
    --ink: #3a3a3a;
    --paper: #ffffff;
    --backdrop: #3b2618;
    --faint-blue: rgba(26, 143, 207, 0.12);
  }
  * { box-sizing: border-box; margin: 0; padding: 0; }
  html, body { width: 848px; height: 1200px; overflow: hidden; background: var(--backdrop); }
  body { font-family: "Source Sans 3", "Myriad Pro", Arial, sans-serif; color: var(--ink); }

  .letterhead {
    position: relative;
    width: 848px;
    height: 1200px;
    background: var(--paper);
    overflow: hidden;
  }
  .side-band { position: absolute; inset: 0; width: 848px; height: 1200px; }

  .brand {
    position: absolute;
    left: 82px; top: 110px;
    display: flex; align-items: center; gap: 14px;
  }
  .brand-dot { flex: none; width: 34px; height: 34px; border-radius: 50%; background: var(--blue); }
  .brand-name {
    font-size: 40px; font-weight: 700; line-height: 1;
    color: var(--blue); letter-spacing: 0.5px;
  }

  .sender {
    position: absolute;
    left: 511px; top: 52px;
    font-size: 12.5px; line-height: 1.4;
    font-style: normal;
  }
  .sender-tagline {
    color: var(--orange); font-weight: 700; font-size: 14.5px; line-height: 1.3;
    margin-bottom: 14px;
  }

  .watermark {
    position: absolute;
    left: 230px; top: 560px;
    font-size: 150px; font-weight: 700; line-height: 1;
    color: var(--faint-blue); letter-spacing: 4px;
  }

  .divisions {
    position: absolute;
    left: 0; width: 695px; top: 1115px;
    text-align: center;
  }
  .division-list { font-size: 13px; font-weight: 700; color: var(--orange); }
  .division-list .sep { color: var(--blue); margin: 0 6px; }
  .division-legal { font-size: 9.5px; font-weight: 600; color: var(--ink); margin-top: 3px; }

  .business-card {
    position: absolute;
    left: 60px; top: 640px;
    width: 500px; height: 300px;
    border-radius: 18px;
    overflow: hidden;
    background: var(--paper);
    box-shadow: 0 0 0 1px #e2e2e2;
  }
  .card-shape { position: absolute; inset: 0; width: 500px; height: 300px; }
  .card-brand {
    position: absolute; left: 26px; top: 160px;
    display: flex; align-items: center; gap: 10px;
  }
  .card-brand .brand-dot { width: 22px; height: 22px; }
  .card-brand .brand-name { font-size: 24px; line-height: 1.05; }
  .card-details {
    position: absolute; left: 270px; top: 50px;
    color: var(--paper);
  }
  .card-holder { color: var(--yellow); font-size: 26px; font-weight: 700; margin-bottom: 26px; }
  .contact-line { display: flex; align-items: flex-start; gap: 10px; font-size: 17px; line-height: 1.15; margin-bottom: 8px; }
  .contact-line svg { flex: none; width: 16px; height: 16px; margin-top: 2px; }
</style>
</head>
<body>
  <main class="letterhead">
    <svg class="side-band" viewBox="0 0 848 1200" aria-hidden="true">
      <path d="M767 0 C 820 180, 830 520, 806 820 C 790 1000, 740 1120, 690 1200 L 848 1200 L 848 0 Z" fill="#f58a1f"/>
      <path d="M773 0 C 826 180, 836 520, 812 820 C 796 1000, 752 1120, 706 1200 L 848 1200 L 848 0 Z" fill="#ef5a24"/>
      <path d="M779 0 C 832 180, 842 520, 818 820 C 802 1000, 764 1120, 720 1200 L 848 1200 L 848 0 Z" fill="var(--blue)"/>
      <path d="M800 0 C 848 200, 848 600, 848 700 L 848 0 Z" fill="#2aa3dd" opacity="0.6"/>
    </svg>

    <div class="brand">
      <span class="brand-dot"></span>
      <span class="brand-name">Kora International</span>
    </div>

    <address class="sender">
      <p class="sender-tagline">Supply &amp; Management<br>of Infrastructure &amp; Logistics</p>
      <p>P.O. Box 482 Hillcrest QLD 4118</p>
      <p>P.O. Box 731 Marsden NSW 2290</p>
      <p>Ph. 0400 555 012</p>
      <p>Email. info@kora.example</p>
    </address>

    <div class="watermark" aria-hidden="true">KORA</div>

    <section class="business-card" aria-label="Business card">
      <svg class="card-shape" viewBox="0 0 500 300" aria-hidden="true">
        <path d="M230 0 C 200 90, 190 200, 225 300 L 500 300 L 500 0 Z" fill="var(--orange)"/>
        <path d="M240 0 C 210 90, 200 200, 235 300 L 500 300 L 500 0 Z" fill="var(--red-orange)"/>
        <path d="M248 0 C 218 90, 208 200, 243 300 L 500 300 L 500 0 Z" fill="var(--blue)"/>
      </svg>
      <div class="card-brand">
        <span class="brand-dot"></span>
        <span class="brand-name">Kora<br>International</span>
      </div>
      <div class="card-details">
        <p class="card-holder">Dale Mercer</p>
        <p class="contact-line">
          <svg viewBox="0 0 16 16"><rect x="4" y="1" width="8" height="14" rx="1.5" fill="none" stroke="#f7941d" stroke-width="1.6"/><circle cx="8" cy="12.5" r="0.9" fill="#f7941d"/></svg>
          +61 400555012
        </p>
        <p class="contact-line">
          <svg viewBox="0 0 16 16"><circle cx="8" cy="8" r="3" fill="none" stroke="#f7941d" stroke-width="1.8"/><path d="M11 6v3.5c0 1.5 3 1.5 3-1A6 6 0 1 0 10.5 13.5" fill="none" stroke="#f7941d" stroke-width="1.8"/></svg>
          dale@kora.example
        </p>
        <p class="contact-line">
          <svg viewBox="0 0 16 16"><rect x="1" y="3" width="14" height="10" rx="1" fill="#f7941d"/><path d="M1.5 3.5 8 9l6.5-5.5" fill="none" stroke="#1a8fcf" stroke-width="1.3"/></svg>
          <span>P.O. Box 482<br>Hillcrest QLD 4118</span>
        </p>
      </div>
    </section>

    <footer class="divisions">
      <p class="division-list">
        KORA Film Services<span class="sep">●</span>KORA Pilot Escorts<span class="sep">●</span>KORA Tour Management<span class="sep">●</span>KORA Driver
      </p>
      <p class="division-legal">are divisions of KORA International Pty Ltd. ACN 000 123 456 &nbsp;ABN 00 000 123 456</p>
    </footer>
  </main>
</body>
</html>
```